KIVO 248
I need double sided standard sized Business Card [3.5" x 2"]
Open to designers choice
Modern
Pavel Rudakovsky
PO BOX 7132
Lornvale, CA 90318
pavel@tumq4.com
kivo248.com

```html
<!DOCTYPE html>
<html lang="en">
<head>
<meta charset="utf-8">
<title>KIVO 248 — Business Card</title>
<link href="https://fonts.googleapis.com/css2?family=Michroma&display=swap" rel="stylesheet">
<style>
  :root {
    --backdrop: #e6e4e2;
    --card-top: #f4f4f3;
    --card-mid: #dcdcdc;
    --card-edge: #c9c9c9;
    --orange: #ef6a2c;
    --orange-deep: #e0421d;
    --orange-light: #f6853a;
    --ink-white: #fff4ec;
    --notch: #3a3a3a;
    --rail: #8d8d8d;
    --rail-light: #e8e8e8;
  }
  * { margin: 0; padding: 0; box-sizing: border-box; }
  html, body { width: 1200px; height: 768px; overflow: hidden; background: var(--backdrop); }
  body { font-family: "Michroma", sans-serif; }

  .card {
    position: absolute; left: 75px; top: 84px; width: 1050px; height: 600px;
    border-radius: 14px; overflow: hidden;
    background: linear-gradient(180deg, var(--card-top) 0%, var(--card-mid) 60%, var(--card-edge) 100%);
    box-shadow: 0 14px 40px rgba(0,0,0,.18);
  }

  .brand {
    position: absolute; left: 205px; top: 52px; height: 100px;
    display: flex; align-items: center; gap: 26px;
  }
  .brand-mark {
    width: 96px; height: 96px; border-radius: 16px; background: var(--orange);
  }
  .brand-name {
    font-size: 64px; color: var(--orange); letter-spacing: 2px; line-height: 1;
  }

  .band {
    position: absolute; left: 0; top: 222px; width: 100%; height: 216px;
    background: linear-gradient(90deg, var(--orange-deep) 0%, var(--orange) 45%, var(--orange-light) 100%);
  }
  .band-notch { position: absolute; left: 138px; top: 222px; width: 36px; height: 20px; }

  .rail {
    position: absolute; left: 0; top: 446px; width: 100%; height: 10px;
    background: linear-gradient(180deg, var(--rail-light), var(--rail) 60%, var(--rail-light));
  }

  .holder { position: absolute; left: 58px; top: 276px; color: var(--ink-white); }
  .holder-name { font-size: 21px; letter-spacing: 1.5px; }
  .holder-title { font-size: 19px; letter-spacing: 1.5px; margin-top: 8px; }

  .divider {
    position: absolute; left: 585px; top: 240px; width: 1px; height: 180px;
    background: rgba(255,244,236,.45);
  }

  .contacts {
    position: absolute; left: 605px; top: 232px; list-style: none; color: var(--ink-white);
  }
  .contacts li {
    display: flex; align-items: center; gap: 14px;
    height: 28px; font-size: 14px; letter-spacing: 1.5px; text-transform: uppercase;
    white-space: nowrap;
  }
  .contacts svg { width: 18px; height: 18px; flex: none; }
</style>
</head>
<body>
  <main class="card">
    <div class="brand">
      <div class="brand-mark"></div>
      <div class="brand-name">kivo248</div>
    </div>

    <div class="band"></div>
    <svg class="band-notch" viewBox="0 0 36 20"><polygon points="0,0 36,0 18,20" fill="var(--notch)"/></svg>
    <div class="rail"></div>

    <div class="holder">
      <p class="holder-name">Pavel Rudakovsky</p>
      <p class="holder-title">CEO</p>
    </div>

    <div class="divider"></div>

    <ul class="contacts">
      <li><svg viewBox="0 0 18 18"><circle cx="9" cy="9" r="9" fill="#fff"/><path d="M9 4a3 3 0 0 1 3 3c0 2.5-3 6-3 6s-3-3.5-3-6a3 3 0 0 1 3-3z" fill="var(--orange)"/></svg>PO BOX 7132</li>
      <li><svg viewBox="0 0 18 18"><circle cx="9" cy="9" r="9" fill="#fff"/><path d="M9 4a3 3 0 0 1 3 3c0 2.5-3 6-3 6s-3-3.5-3-6a3 3 0 0 1 3-3z" fill="var(--orange)"/></svg>Lornvale, CA 90318</li>
      <li><svg viewBox="0 0 18 18"><circle cx="9" cy="9" r="9" fill="#fff"/><rect x="6" y="4" width="6" height="10" rx="1.2" fill="var(--orange)"/></svg>5550142873</li>
      <li><svg viewBox="0 0 18 18"><circle cx="9" cy="9" r="9" fill="#fff"/><rect x="6" y="4" width="6" height="10" rx="1.2" fill="var(--orange)"/></svg>5550179246</li>
      <li><svg viewBox="0 0 18 18"><circle cx="9" cy="9" r="9" fill="#fff"/><rect x="6" y="4" width="6" height="10" rx="1.2" fill="var(--orange)"/></svg>5550163318</li>
      <li><svg viewBox="0 0 18 18"><circle cx="9" cy="9" r="9" fill="#fff"/><rect x="4.5" y="5.5" width="9" height="7" fill="var(--orange)"/><path d="M4.5 5.5 9 9.5l4.5-4" stroke="#fff" stroke-width="1" fill="none"/></svg>pavel@tumq4.com</li>
      <li><svg viewBox="0 0 18 18"><circle cx="9" cy="9" r="9" fill="#fff"/><circle cx="9" cy="9" r="4.5" fill="none" stroke="var(--orange)" stroke-width="1.4"/><path d="M4.5 9h9M9 4.5v9" stroke="var(--orange)" stroke-width="1"/></svg>www.kivo248.com</li>
    </ul>
  </main>
</body>
</html>
```